Stationary Design (using existing logo)

Stationary (print and electronic version for Word/email), envelope, and fax cover. All companies are part of same family or course so designs can be the same, or essentially the same. Use the logos attached, same font and colors.

Target Market(s)

Real estate professionals. Investors and other property owners. Financial professionals.

Industry/Entity Type

Real Estate

Font styles to use
Serif

Requirements
Must have
• Should be a serious, sophisticated design in colors that match the business cards we uploaded. Design needs to match the color and fonts in the attached business cards. Can use the same design for each company, just change logo and color.
Should not have
• Nothing quirky or cute.

```html
<!DOCTYPE html>
<html lang="en">
<head>
<meta charset="utf-8">
<title>Meridale Realty Group – Stationery Set</title>
<link rel="stylesheet" href="https://fonts.googleapis.com/css2?family=Libre+Baskerville&family=Arimo:wght@400;700&display=swap">
<style>
  :root{
    --navy:#233c7c;
    --board:#c4c4c4;
    --paper:#ffffff;
    --rule:#8a8a8a;
    --ink:#222;
    --faint:#ececec;
    --serif:"Libre Baskerville", Georgia, serif;
    --sans:"Arimo", Arial, sans-serif;
  }
  *{box-sizing:border-box;margin:0;padding:0}
  html,body{width:1200px;height:1200px;overflow:hidden;background:var(--board)}
  .board{position:relative;width:1200px;height:1200px}
  .sheet{position:absolute;background:var(--paper);box-shadow:8px 8px 10px rgba(0,0,0,.28);overflow:hidden}
  .letterhead{left:92px;top:101px;width:490px;height:635px}
  .faxcover{left:620px;top:101px;width:491px;height:635px}
  .envelope-front{left:123px;top:818px;width:459px;height:230px}
  .envelope-back{left:620px;top:817px;width:457px;height:228px}
  .footer-band{position:absolute;left:0;right:0;bottom:0;height:22px;background:var(--navy)}
  .envelope-front .footer-band{height:18px}

  .brand{position:absolute;font-family:var(--serif);color:var(--navy);text-align:center;line-height:1}
  .brand .brand-name{display:block;font-size:21px;letter-spacing:1px;border-bottom:1px solid var(--navy);padding-bottom:2px}
  .brand .brand-sub{display:block;font-size:7.5px;letter-spacing:1.6px;margin-top:3px}
  .letterhead .brand,.faxcover .brand{left:46px;top:40px;width:142px}
  .envelope-front .brand{left:17px;top:27px;width:90px}
  .envelope-front .brand .brand-name{font-size:13px;letter-spacing:.5px}
  .envelope-front .brand .brand-sub{font-size:5px;letter-spacing:1px;margin-top:2px}

  .contact{position:absolute;left:361px;top:22px;border-left:1px solid var(--rule);padding-left:8px;font-family:var(--serif);font-size:6.2px;line-height:1.35;color:var(--ink)}
  .contact .web{margin-top:5px}
  .contact address{font-style:normal;color:var(--navy);margin-top:5px}

  .return-address{position:absolute;left:17px;top:67px;font-family:var(--serif);font-size:7.2px;line-height:1.4;color:var(--navy);font-style:normal}

  .watermark{position:absolute;font-family:var(--serif);color:var(--faint);font-size:30px;letter-spacing:2px;text-align:center;width:100%}
  .letterhead .watermark{top:265px}

  .fax-table{position:absolute;left:39px;top:121px;width:412px;border-collapse:collapse;font-family:var(--sans);font-size:7px;font-weight:700;color:var(--ink)}
  .fax-table td{border:1px solid var(--rule);height:14.2px;padding:0 5px;vertical-align:middle}
  .fax-table .label{width:46px}
  .fax-table .field{width:170px}

  .comments{position:absolute;left:39px;top:206px;width:412px;height:358px;border:1px solid var(--rule)}
  .status-bar{display:flex;height:15px;background:var(--navy);font-family:var(--sans);font-size:7px;font-weight:700;color:#fff}
  .status-bar span{display:flex;align-items:center;padding-left:15px;border-right:1px solid #fff;gap:3px}
  .status-bar span:last-child{border-right:0}
  .status-bar i{display:inline-block;width:5px;height:6px;border:.8px solid #fff}
  .comments-label{font-family:var(--sans);font-size:7px;text-align:center;margin-top:11px;color:var(--ink)}
  .comments .watermark{top:160px}

  .flap{position:absolute;left:0;top:0}
  .envelope-back .seal-name{position:absolute;top:32px;width:100%;text-align:center;font-family:var(--serif);font-size:11px;color:var(--rule);letter-spacing:1px}
</style>
</head>
<body>
<main class="board">

  <section class="sheet letterhead" aria-label="Letterhead">
    <div class="brand"><span class="brand-name">MERIDALE</span><span class="brand-sub">REALTY GROUP</span></div>
    <div class="contact">
      <div>555.010.2286</div>
      <div>555.010.2287 (Fax)</div>
      <div class="web">www.meridalerealty.com</div>
      <address>1480 W Harlow Ave.<br>Fairhaven, IL 60600</address>
    </div>
    <div class="watermark">MERIDALE</div>
    <div class="footer-band"></div>
  </section>

  <section class="sheet faxcover" aria-label="Fax cover sheet">
    <div class="brand"><span class="brand-name">MERIDALE</span><span class="brand-sub">REALTY GROUP</span></div>
    <div class="contact">
      <div>555.010.2286</div>
      <div>555.010.2287 (Fax)</div>
      <div class="web">www.meridalerealty.com</div>
      <address>1480 W Harlow Ave.<br>Fairhaven, IL 60600</address>
    </div>
    <table class="fax-table">
      <tr><td class="label">To:</td><td class="field"></td><td class="label">From:</td><td></td></tr>
      <tr><td class="label">Fax:</td><td class="field"></td><td class="label">Pages:</td><td></td></tr>
      <tr><td class="label">Phone:</td><td class="field"></td><td class="label">Date:</td><td></td></tr>
      <tr><td class="label">Re:</td><td class="field"></td><td class="label">CC:</td><td></td></tr>
    </table>
    <div class="comments">
      <div class="status-bar">
        <span style="width:76px"><i></i>Urgent</span>
        <span style="width:83px"><i></i>For Review</span>
        <span style="width:96px"><i></i>Please Comment</span>
        <span style="width:81px"><i></i>Please Reply</span>
        <span style="flex:1;padding-left:11px"><i></i>Confidential</span>
      </div>
      <div class="comments-label">COMMENTS:</div>
      <div class="watermark">MERIDALE</div>
    </div>
    <div class="footer-band"></div>
  </section>

  <section class="sheet envelope-front" aria-label="Envelope front">
    <div class="brand"><span class="brand-name">MERIDALE</span><span class="brand-sub">REALTY GROUP</span></div>
    <address class="return-address">1480 W Harlow Ave.<br>Fairhaven, IL 60600</address>
    <div class="footer-band"></div>
  </section>

  <section class="sheet envelope-back" aria-label="Envelope back">
    <svg class="flap" width="457" height="70" viewBox="0 0 457 70">
      <path d="M2 0 C20 40 30 62 42 62 L412 62 C424 62 438 40 456 0" fill="none" stroke="var(--rule)" stroke-width="1"/>
    </svg>
    <div class="seal-name">MERIDALE</div>
  </section>

</main>
</body>
</html>
```